Wooden Floor Website

I'd like a Modern and crisp site with emphasis on the site being easy to navigate through - services that we offer, gallery of previous work, history, who we are, contact, etc
https://tmqrvx8219067-my.dokshelfbox.net/:b:/g/personal/marcus_bellhaven_co_uk/QWT7K2_pmRsNaHXdovtYBeLWCKjuP9e3F6kRMZbqUwnPzs

Coding

Coded - Design and coding required

Number of Pages Required

5+ page

Requirements
Must have
• Word Press Site

```html
<!DOCTYPE html>
<html lang="en">
<head>
<meta charset="utf-8">
<title>Bellhaven Wooden Floors – Website Pages</title>
<link href="https://fonts.googleapis.com/css2?family=Open+Sans:wght@400;600;700&family=Montserrat:wght@400;500;600&display=swap" rel="stylesheet">
<style>
:root{
  --stage:#c6cacd;
  --page:#ffffff;
  --page-soft:#f6f6f6;
  --ink:#2b2b2b;
  --muted:#6f6f6f;
  --line:#e2e2e2;
  --wood-orange:#d9761f;
  --wood-light:#e8a24a;
  --oak:#b89a76;
  --oak-dark:#6e5a48;
  --grey-photo:#8d8d8d;
  --lime:#c7e21b;
  --brown-btn:#4a1f12;
  --teal:#4fb7b0;
  --shadow:0 10px 30px rgba(0,0,0,.25);
}
*{box-sizing:border-box;margin:0;padding:0}
html,body{width:1200px;height:839px;overflow:hidden}
body{background:var(--stage);font-family:"Open Sans",sans-serif;color:var(--ink);position:relative}
.page{position:absolute;top:28px;height:784px;background:var(--page);box-shadow:var(--shadow);overflow:hidden}
.page--left{left:20px;width:360px}
.page--home{left:400px;width:400px}
.page--right{left:820px;width:360px}
.photo{background:linear-gradient(135deg,var(--grey-photo),#c9c9c9)}
.photo--oak{background:linear-gradient(135deg,var(--oak),#d8c2a3)}
.photo--dark{background:linear-gradient(135deg,#3f4a55,var(--oak))}
.photo--green{background:linear-gradient(135deg,#3f5a4a,#9b8d78)}
.strip{display:grid;grid-template-columns:repeat(4,1fr);height:62px}
.section-title{font-family:"Montserrat",sans-serif;font-weight:600;text-align:center;font-size:13px;color:var(--ink)}
.rule{width:28px;height:2px;background:var(--muted);margin:6px auto 0}
.small{font-size:6.5px;line-height:1.5;color:var(--muted)}
h3{font-family:"Montserrat",sans-serif;font-size:12px;font-weight:600;line-height:1.25}
h4{font-size:7px;font-weight:700;margin-bottom:4px}

/* left page */
.faq{position:relative;height:300px;padding:18px 20px}
.faq__wood{position:absolute;left:0;right:0;top:70px;bottom:0;background:linear-gradient(160deg,var(--wood-light),var(--wood-orange))}
.faq__content{position:relative}
.faq__title{text-align:right;font-size:10px;font-weight:700;margin-bottom:18px}
.faq__cols{display:grid;grid-template-columns:1fr 1fr;gap:16px}
.faq__q{font-size:6.5px;font-weight:700;margin:6px 0 3px}
.faq__feature{position:relative;margin-top:36px;width:200px}
.faq__feature h3{color:#3b2a14;font-size:10px}
.press{height:70px;display:flex;justify-content:center;align-items:center;gap:30px}
.press__badge{width:48px;height:14px;background:#b9b9b9}
.dots{display:flex;justify-content:center;gap:5px;margin-top:-14px}
.dots span{width:4px;height:4px;border-radius:50%;border:1px solid #999}
.dots span.on{background:#555}
.work-intro{height:150px;background:var(--page-soft);padding-top:58px}

/* home page */
.hero{position:relative;height:270px}
.hero__image{position:absolute;inset:0;background:linear-gradient(160deg,#e2e2e2 0%,#bdbdbd 55%,#5c5c5c 100%)}
.nav{position:absolute;top:10px;right:10px;display:flex;gap:8px;font-size:5px;text-transform:uppercase;color:#333;letter-spacing:.3px;align-items:center}
.nav .active{border-bottom:1px solid var(--teal)}
.brand{position:absolute;top:60px;left:90px;display:flex;align-items:center;gap:8px}
.brand__mark{width:12px;height:12px;background:#333}
.brand__name{font-family:"Montserrat",sans-serif;font-weight:500;letter-spacing:2px;font-size:15px;color:#333}
.apply{position:absolute;top:120px;left:200px;width:130px;padding:8px;background:rgba(255,255,255,.18)}
.apply__title{font-size:7px;color:#fff;margin-bottom:6px}
.apply__field{height:12px;border-bottom:1px solid rgba(255,255,255,.7);font-size:5px;color:#fff;margin-bottom:6px;padding-top:3px}
.apply__btn{display:block;margin:8px auto 0;background:var(--lime);font-size:5px;font-weight:700;padding:4px 8px;width:max-content}
.intro{display:grid;grid-template-columns:140px 1fr;gap:12px;padding:18px 14px 18px 95px;height:130px;position:relative}
.intro__leaf{position:absolute;left:0;top:0;width:90px;height:40px;background:linear-gradient(90deg,#5a8a2c,#9bc15a)}
.benefits{display:grid;grid-template-columns:repeat(3,1fr);gap:6px}
.benefit .photo{height:36px;margin-bottom:6px}
.features{background:var(--page-soft);padding:22px 20px 0;height:218px}
.features__body{display:grid;grid-template-columns:130px 1fr;gap:22px;margin-top:16px}
.features__img{height:120px}
.feature{display:flex;gap:8px;margin-bottom:12px}
.feature svg{flex:none}

/* right page */
.work{padding:40px 10px 0;height:430px;background:var(--page-soft)}
.grid{display:grid;grid-template-columns:repeat(4,1fr);margin-top:56px;height:180px}
.load{display:block;width:max-content;margin:30px auto 0;background:var(--brown-btn);color:#fff;font-size:5px;font-weight:700;padding:5px 9px;letter-spacing:.4px}
.contact{position:relative;height:354px;background:linear-gradient(170deg,#c8641b,var(--wood-orange))}
.contact__card{position:absolute;left:0;top:14px;width:220px;height:140px;background:#fff;padding:8px}
.contact__map{position:absolute;left:0;top:0;width:70px;height:48px;background:#e5e3dc}
.contact__info{margin-left:72px}
.contact__label{font-size:5px;font-weight:700;letter-spacing:.6px;margin-bottom:4px}
.contact__input{height:10px;border-bottom:1px solid var(--wood-orange);margin-top:10px}
.contact__brand{position:absolute;right:20px;top:40px;display:flex;align-items:center;gap:6px}
.contact__brand .brand__name{font-size:10px;color:#fff;letter-spacing:1px}
.contact__trees{position:absolute;right:0;bottom:0;width:200px;height:150px;background:linear-gradient(180deg,rgba(74,110,58,0),#4a6e3a 70%)}
</style>
</head>
<body>

<section class="page page--left" aria-label="FAQ and press page">
  <div class="strip">
    <div class="photo" role="img" aria-label="Interior with shelves"></div>
    <div class="photo photo--oak" role="img" aria-label="Herringbone wood floor"></div>
    <div class="photo" role="img" aria-label="Grey plank floor"></div>
    <div class="photo photo--dark" role="img" aria-label="Dark oak floor"></div>
  </div>
  <div class="faq">
    <div class="faq__wood" role="img" aria-label="Orange wood grain texture"></div>
    <div class="faq__content">
      <p class="faq__title">Frequently Asked Questions</p>
      <div class="faq__cols">
        <div>
          <p class="faq__q">How does the free trial work?</p>
          <p class="small">Lorem ipsum dolor sit amet, consectetur adipiscing elit sed do eiusmod tempor.</p>
          <p class="faq__q">Can I switch plans later?</p>
          <p class="small">Lorem ipsum dolor sit amet, consectetur adipiscing elit.</p>
        </div>
        <div>
          <p class="faq__q">Do I need to choose?</p>
          <p class="small">Lorem ipsum dolor sit amet, consectetur elit.</p>
          <p class="faq__q">What payment is accepted?</p>
          <p class="small">Lorem ipsum dolor sit amet elit.</p>
        </div>
      </div>
      <div class="faq__feature">
        <h3>This is your first amazing feature and it's awesome!</h3>
        <p class="small" style="color:#4a3418;margin-top:8px">Lorem ipsum dolor sit amet, consectetur adipiscing elit, sed do eiusmod tempor incididunt ut labore.</p>
      </div>
    </div>
  </div>
  <div class="press">
    <span class="press__badge"></span><span class="press__badge"></span><span class="press__badge"></span>
  </div>
  <div class="dots"><span></span><span class="on"></span><span></span><span></span></div>
  <div class="work-intro">
    <p class="section-title">Our Amazing Work</p>
    <div class="rule"></div>
  </div>
  <div class="strip">
    <div class="photo photo--oak" role="img" aria-label="Bright living room floor"></div>
    <div class="photo" role="img" aria-label="Grey oak floor"></div>
    <div class="photo photo--oak" role="img" aria-label="Natural oak floor"></div>
    <div class="photo photo--dark" role="img" aria-label="Blue room with oak floor"></div>
  </div>
</section>

<section class="page page--home" aria-label="Home page">
  <div class="hero">
    <div class="hero__image" role="img" aria-label="White living room with dark wooden floor and large window"></div>
    <nav class="nav">
      <span class="active">Home</span><span>About</span><span>Skills</span><span>Service</span><span>Work</span><span>Testimonial</span><span>Blog</span><span>Team</span><span>Contact</span>
      <svg width="7" height="7" viewBox="0 0 10 10"><circle cx="4" cy="4" r="3" fill="none" stroke="#333" stroke-width="1.4"/><line x1="6.2" y1="6.2" x2="9" y2="9" stroke="#333" stroke-width="1.4"/></svg>
    </nav>
    <div class="brand"><span class="brand__mark"></span><span class="brand__name">BELLHAVEN</span></div>
    <form class="apply">
      <p class="apply__title">Apply Now for Free</p>
      <div class="apply__field">hello@bellhaven.co.uk</div>
      <div class="apply__field">Your password</div>
      <div class="apply__field">123 456 789</div>
      <span class="apply__btn">APPLY FOR FREE TRIAL</span>
    </form>
  </div>
  <div class="intro">
    <div class="intro__leaf" role="img" aria-label="Green leaves"></div>
    <div>
      <h3>This is your first amazing feature and it's awesome!</h3>
      <p class="small" style="margin-top:8px">Lorem ipsum dolor sit amet, consectetur adipiscing elit, sed do eiusmod tempor incididunt.</p>
      <p class="small" style="margin-top:6px">Duis aute irure dolor in reprehenderit in voluptate velit esse cillum dolore eu fugiat nulla pariatur.</p>
    </div>
    <div class="benefits">
      <div class="benefit"><div class="photo photo--oak" role="img" aria-label="Kitchen with oak floor"></div><h4>First Benefit</h4><p class="small">Lorem ipsum dolor sit amet, adipiscing elit.</p></div>
      <div class="benefit"><div class="photo photo--green" role="img" aria-label="Green room with wood floor"></div><h4>Second Benefit</h4><p class="small">Ut enim ad minim veniam, quis nostrud.</p></div>
      <div class="benefit"><div class="photo" role="img" aria-label="Close view of oak planks"></div><h4>Third Benefit</h4><p class="small">Ut enim ad minim veniam, quis nostrud.</p></div>
    </div>
  </div>
  <div class="features">
    <p class="section-title">Features</p>
    <p class="small" style="text-align:center;margin-top:6px">Lorem ipsum dolor sit amet, consectetur adipiscing elit,<br>sed do eiusmod tempor incididunt ut labore et dolore</p>
    <div class="features__body">
      <div class="features__img photo--oak" role="img" aria-label="Oak floor with patterned rug and plant"></div>
      <div>
        <div class="feature"><svg width="10" height="10" viewBox="0 0 10 10"><circle cx="5" cy="5" r="4" fill="none" stroke="#777"/></svg><div><h4>Feature number 1</h4><p class="small">Lorem ipsum dolor sit amet, consectetur adipiscing elit, sed do eiusmod tempor.</p></div></div>
        <div class="feature"><svg width="10" height="10" viewBox="0 0 10 10"><circle cx="5" cy="5" r="4" fill="none" stroke="#777"/></svg><div><h4>Feature number 2</h4><p class="small">Lorem ipsum dolor sit amet, consectetur adipiscing elit, sed do eiusmod tempor.</p></div></div>
        <div class="feature"><svg width="10" height="10" viewBox="0 0 10 10"><circle cx="5" cy="5" r="4" fill="none" stroke="#777"/></svg><div><h4>Feature number 3</h4><p class="small">Lorem ipsum dolor sit amet, consectetur adipiscing elit, sed do eiusmod tempor.</p></div></div>
      </div>
    </div>
  </div>
  <div class="strip" style="height:166px">
    <div class="photo" role="img" aria-label="Interior with shelves"></div>
    <div class="photo photo--oak" role="img" aria-label="Grey herringbone floor"></div>
    <div class="photo" role="img" aria-label="Bright room with frames"></div>
    <div class="photo photo--dark" role="img" aria-label="Dark plank floor"></div>
  </div>
</section>

<section class="page page--right" aria-label="Work and contact page">
  <div class="work">
    <p class="section-title">Our Amazing Work</p>
    <div class="rule"></div>
    <div class="grid">
      <div class="photo" role="img" aria-label="Living room with oak floor"></div>
      <div class="photo photo--oak" role="img" aria-label="Orange chair on oak floor"></div>
      <div class="photo" role="img" aria-label="Pale room with round table"></div>
      <div class="photo photo--dark" role="img" aria-label="Blue room with rug"></div>
      <div class="photo photo--oak" role="img" aria-label="Orange sofa room"></div>
      <div class="photo photo--dark" role="img" aria-label="Navy kitchen"></div>
      <div class="photo photo--dark" role="img" aria-label="Blue chair on oak floor"></div>
      <div class="photo photo--oak" role="img" aria-label="Close oak planks"></div>
      <div class="photo photo--green" role="img" aria-label="Green room with wood floor"></div>
      <div class="photo" role="img" aria-label="Grey oak floor"></div>
      <div class="photo photo--oak" role="img" aria-label="Oak floor with blanket"></div>
      <div class="photo photo--dark" role="img" aria-label="Dining room with oak floor"></div>
    </div>
    <span class="load">+ LOAD MORE</span>
  </div>
  <div class="contact" role="group" aria-label="Contact">
    <div class="contact__card">
      <div class="contact__map" role="img" aria-label="Street map"></div>
      <div class="contact__info">
        <p class="contact__label">CONTACT INFORMATION</p>
        <p class="small">Visit our showroom or send us a note.</p>
        <p class="small">12 Mill Lane, Bellhaven</p>
        <p class="small">hello@bellhaven.co.uk</p>
      </div>
      <div class="contact__input" style="margin-top:22px"></div>
      <div class="contact__input"></div>
      <div class="contact__input"></div>
    </div>
    <div class="contact__brand"><span class="brand__mark" style="background:#fff"></span><span class="brand__name">BELLHAVEN</span></div>
    <div class="contact__trees" role="img" aria-label="Row of green trees on grass"></div>
  </div>
</section>

</body>
</html>
```